Cocktail Menu for my Breakfast Cafe

I would like a simple drink menu designed. I have uploaded the info of names and prices as well as our restaurant logo - We are an old meets new kind of theme - lots of antiques in our restaurant with buffalo heads - wood everywhere. I would just like something simple and rustic looking with a modern twist - the colors that I would like are neutral tones - browns/woods / Taupes etc

Target Market(s)

Variety - families and trendy hipsters on the weekend and Business People during the week

Industry/Entity Type

Cafe

Font styles to use
Serif

Colors

Designer to choose colors to be used in the design.

Requirements
Must have
• must fit on 127 X 178 paper - it will be a table tent menu so there will need to be a front and back design - The front should have the entire drink menu and the back can just be a solid color or maybe something with our logo
Nice to have
• Traditional with a modern twist
• Saloon style
• wood motif perhaps?
Should not have
• I'm pretty flexible with ideas

```html
<!DOCTYPE html>
<html lang="en">
<head>
<meta charset="utf-8">
<title>Wet Your Whistle – Drink Menu</title>
<link rel="stylesheet" href="https://fonts.googleapis.com/css2?family=Rye&family=IM+Fell+DW+Pica+SC&family=Old+Standard+TT:wght@400;700&display=swap">
<style>
  :root {
    --paper: #ebdfc7;
    --paper-edge: #d9c8a8;
    --ink: #2a241c;
    --ink-soft: #4a4034;
    --badge: #8f8270;
    --art-dark: #3a3128;
    --art-mid: #7a6c58;
  }
  html, body { margin: 0; padding: 0; overflow: hidden; }
  body { width: 857px; height: 1200px; }
  .menu {
    position: relative;
    width: 857px; height: 1200px; overflow: hidden;
    background: radial-gradient(ellipse at 60% 40%, #f1e6d0 0%, var(--paper) 55%, var(--paper-edge) 100%);
    color: var(--ink);
  }
  .menu-title {
    position: absolute; left: 50px; top: 48px; margin: 0;
    font-family: "Rye", serif; font-weight: 400;
    font-size: 66px; line-height: 76px; letter-spacing: 1px;
    color: var(--ink); white-space: nowrap;
  }
  .feature-art {
    position: absolute; left: 0; top: 222px; width: 436px; height: 922px;
    background: radial-gradient(ellipse at 15% 55%, var(--art-dark) 0%, var(--art-mid) 45%, rgba(122,108,88,0.35) 70%, rgba(235,223,199,0) 85%);
  }
  .drink-name-frame {
    position: absolute; left: 478px; width: 312px;
    border-top: 2px solid var(--ink);
    border-bottom: 2px solid var(--ink);
    box-sizing: border-box;
  }
  .drink-name-frame::before {
    content: ""; position: absolute; left: 0; top: 6px; bottom: 6px;
    border-left: 2px solid var(--ink);
  }
  .drink-number {
    position: absolute; left: -11px; top: 50%; transform: translateY(-50%);
    width: 20px; height: 20px; border-radius: 50%;
    background: var(--badge); color: #efe4cf;
    font-family: "Old Standard TT", serif; font-size: 12px; line-height: 20px; text-align: center;
  }
  .drink-name {
    margin: 0; padding-left: 24px;
    font-family: "IM Fell DW Pica SC", serif; font-weight: 400;
    font-size: 40px; line-height: 46px; color: var(--ink);
  }
  .ingredients {
    position: absolute; left: 484px; margin: 0; padding: 0; list-style: none;
    font-family: "Old Standard TT", serif; font-weight: 700;
    font-size: 12.5px; line-height: 19px; text-transform: uppercase; color: var(--ink-soft);
  }
  .price-row {
    position: absolute; left: 504px; margin: 0;
    font-family: "Old Standard TT", serif; color: var(--ink);
    display: flex; align-items: baseline; white-space: nowrap;
  }
  .price-row .size { font-size: 11px; font-variant: small-caps; margin-right: 14px; }
  .price-row .amount { font-size: 21px; }
  .price-row .amount + .size { margin-left: 38px; }
</style>
</head>
<body>
<main class="menu">
  <h1 class="menu-title">WET YOUR<br>WHISTLE</h1>

  <div class="feature-art" role="img" aria-label="Pen-and-ink illustration of a shaggy highland bull with one curved horn"></div>

  <!-- 1 -->
  <div class="drink-name-frame" style="top:34px;height:76px;padding-top:12px;">
    <span class="drink-number">1</span>
    <h2 class="drink-name">Simple Ceasar</h2>
  </div>
  <ul class="ingredients" style="top:134px;">
    <li>Vodka</li><li>Tomaclam</li><li>Worcestershire</li><li>Fuego Sauce</li><li>Pickled Asparagus</li>
  </ul>
  <p class="price-row" style="top:232px;"><span class="size">1 oz</span><span class="amount">7.00</span><span class="size">Buffalo Size</span><span class="amount">11.00</span></p>

  <!-- 2 -->
  <div class="drink-name-frame" style="top:286px;height:128px;padding-top:14px;">
    <span class="drink-number">2</span>
    <h2 class="drink-name">Someone Spiked<br>My Juice!</h2>
  </div>
  <ul class="ingredients" style="top:437px;">
    <li>Vodka</li><li>Orange Juice</li>
  </ul>
  <p class="price-row" style="top:479px;"><span class="size">1 oz</span><span class="amount">6.00</span><span class="size">Buffalo Size</span><span class="amount">10.00</span></p>

  <!-- 3 -->
  <div class="drink-name-frame" style="top:530px;height:124px;padding-top:14px;">
    <span class="drink-number">3</span>
    <h2 class="drink-name">Bramble's N<br>Coffee</h2>
  </div>
  <ul class="ingredients" style="top:678px;">
    <li>Bramble's Liqueur</li><li>Coffee</li>
  </ul>
  <p class="price-row" style="top:720px;"><span class="amount">6.00</span></p>

  <!-- 4 -->
  <div class="drink-name-frame" style="top:773px;height:73px;padding-top:11px;">
    <span class="drink-number">4</span>
    <h2 class="drink-name">Madame Mimosa!</h2>
  </div>
  <ul class="ingredients" style="top:869px;left:482px;">
    <li>200ml Personal Prosecco</li><li>Orange Juice</li><li>Raspberries</li>
  </ul>
  <p class="price-row" style="top:930px;"><span class="amount">11.00</span></p>

  <!-- 5 -->
  <div class="drink-name-frame" style="top:978px;height:73px;padding-top:11px;">
    <span class="drink-number">5</span>
    <h2 class="drink-name">Local Brew</h2>
  </div>
  <ul class="ingredients" style="top:1075px;">
    <li>Hamlet Blonde</li><li>Steamkettle</li><li>Mill Lane Organic</li>
  </ul>
  <p class="price-row" style="top:1136px;"><span class="amount">6.00</span></p>
</main>
</body>
</html>
```